Dental Hygiene referral cards

I am looking to make some referral cards for our hygienists for our dental office. something with our logo and address on the front, and on the back have
hygienist:
__________________
Referred by:
__________________
with a little blurb about what we will give away for a referral.

attached to this is our logo, and a drawing of what im looking for.

I will need this for two of our offices, so just the logo and address will change.

```html
<!DOCTYPE html>
<html lang="en">
<head>
<meta charset="utf-8">
<title>Riverbend Crossing Dental – Referral Card</title>
<link rel="stylesheet" href="https://fonts.googleapis.com/css2?family=Lato:wght@300;400&family=Montserrat:wght@600;700;800&display=swap">
<style>
  :root {
    --backdrop: #294a7b;
    --card: #f4f4f3;
    --brand-blue: #33508f;
    --band-blue: #34528e;
    --band-grey: #9c9c9c;
    --rule-grey: #9a9a9a;
    --ink-dark: #1d1d1d;
    --ink-light: #ffffff;
    --brush-dark: #2a2a2a;
    --brush-mid: #4a4a4a;
  }
  * { margin: 0; padding: 0; box-sizing: border-box; }
  html, body {
    width: 1200px; height: 1000px; overflow: hidden;
    background: var(--backdrop);
  }
  .canvas { position: relative; width: 1200px; height: 1000px; }

  .card {
    position: absolute;
    width: 515px; height: 294px;
    background: var(--card);
    overflow: hidden;
  }
  .card--front { left: 349px; top: 190px; }
  .card--back  { left: 346px; top: 531px; height: 295px; }

  /* Front */
  .brand {
    position: absolute; left: 0; right: 0; top: 44px;
    display: flex; flex-direction: column; align-items: center;
  }
  .brand__dot {
    width: 64px; height: 64px; border-radius: 50%;
    background: var(--band-grey);
    margin-bottom: 22px;
  }
  .brand__name {
    font-family: "Montserrat", sans-serif;
    font-weight: 700;
    color: var(--brand-blue);
    font-size: 33px;
    line-height: 1.12;
    text-align: center;
    letter-spacing: 1px;
    text-transform: uppercase;
  }
  .front-address {
    position: absolute; left: 0; right: 0; top: 248px; height: 20px;
    background: var(--band-blue);
    color: var(--ink-light);
    font-family: "Lato", sans-serif; font-weight: 400;
    font-size: 13.5px; line-height: 20px;
    text-align: right; padding-right: 54px;
  }
  .front-foot {
    position: absolute; left: 0; right: 0; top: 268px; bottom: 0;
    background: var(--band-grey);
  }

  /* Back */
  .field {
    position: absolute; left: 30px; right: 19px;
    display: flex; align-items: flex-end;
    font-family: "Montserrat", sans-serif; font-weight: 600;
    font-size: 19px; color: var(--brand-blue);
  }
  .field--hygienist { top: 36px; left: 32px; }
  .field--referral  { top: 93px; }
  .field__line {
    flex: 1; margin-left: 12px; margin-bottom: 4px;
    border-bottom: 1.5px solid var(--rule-grey);
  }
  .offer {
    position: absolute; left: 0; right: 0; top: 144px; height: 66px;
    background: var(--band-blue);
    color: var(--ink-light);
    font-family: "Montserrat", sans-serif; font-weight: 700;
    font-size: 11.5px; line-height: 18px; letter-spacing: 0.3px;
    text-align: center;
    display: flex; align-items: center; justify-content: center;
    text-transform: uppercase;
  }
  .prize-visual {
    position: absolute; left: 27px; top: 224px; width: 269px; height: 27px;
    border-radius: 4px;
    background: linear-gradient(90deg, var(--brush-dark), var(--brush-mid) 80%, #5c7fa8);
  }
  .prize-title {
    position: absolute; left: 310px; top: 216px;
    font-family: "Montserrat", sans-serif; font-weight: 800;
    font-size: 20px; line-height: 24px;
    color: var(--ink-dark); text-transform: uppercase;
  }
  .prize-title__accent { color: var(--brand-blue); }
  .back-foot {
    position: absolute; left: 0; right: 0; top: 269px; bottom: 0;
    background: var(--band-grey);
  }
</style>
</head>
<body>
<main class="canvas">

  <section class="card card--front" aria-label="Referral card front">
    <div class="brand">
      <div class="brand__dot"></div>
      <div class="brand__name">Riverbend Crossing<br>Dental</div>
    </div>
    <div class="front-address">4120 Harbour Ridge Rd NE #118, Cedarfield, Alberta T4C 1R8</div>
    <div class="front-foot"></div>
  </section>

  <section class="card card--back" aria-label="Referral card back">
    <div class="field field--hygienist">
      <span class="field__label">HYGIENIST:</span>
      <span class="field__line"></span>
    </div>
    <div class="field field--referral">
      <span class="field__label">REFERRED BY:</span>
      <span class="field__line"></span>
    </div>
    <div class="offer">Refer a paitent for an exam and a cleaning and both of<br>you will get a free SmileWave toothbrush!</div>
    <div class="prize-visual" role="img" aria-label="Illustration of an electric toothbrush"></div>
    <div class="prize-title"><span class="prize-title__accent">Free</span> SmileWave<br>Toothbrush!</div>
    <div class="back-foot"></div>
  </section>

</main>
</body>
</html>
```